Label Design for a New Alcoholized Root Beer

Create a design for a new alcoholized root beer. This is a new product category in the USA growing very rapidly. Root Beer is a popular flavor of Cola, but recently, beer manufacturers have added alcohol to it and have created a new product that has gained traction on the market at a tremendous rate.

Root Beer is vintage product that has been around for a hundred years. Consumers of this product are mostly male between the age of 30 to 45. They purchase this product for its nostalgia and vintage look and taste.

This product will be in a standard 355 mL brown bottle.

It is 5.9% abv.

The name of the product is ''Corvel's Hard Root Beer''.

We have uploaded some pictures of traditional root beers to give you an idea of the feel we want our product to have and also, the bottle the product will be filled in.

Target Market(s)

Consumers are male 30-45, same market as craft beer consumers

Industry/Entity Type

Product

Requirements
Must have
• Design must have a vintage feel to it

```html
<!DOCTYPE html>
<html lang="en">
<head>
<meta charset="utf-8">
<title>Corvel's Hard Root Beer – Label</title>
<link rel="stylesheet" href="https://fonts.googleapis.com/css2?family=Oldenburg&family=Tinos&display=swap">
<style>
  :root {
    --backdrop: #e8e4d4;
    --gold-light: #f0e2b4;
    --gold-mid: #e2cf95;
    --gold-deep: #cdb474;
    --brown-dark: #3e2a1d;
    --brown-mid: #6b4a32;
    --seal: #8d6c50;
    --cream: #f3ead2;
    --leaf: #a9835a;
  }
  html, body {
    margin: 0;
    padding: 0;
    width: 1200px;
    height: 1142px;
    overflow: hidden;
    background: var(--backdrop);
  }
  .label-sheet { display: block; width: 1200px; height: 1142px; }
  .brand-name { font-family: "Oldenburg", serif; font-size: 36px; fill: var(--cream); }
  .product-type { font-family: "Oldenburg", serif; font-size: 40px; fill: var(--brown-dark); }
  .volume { font-family: "Tinos", serif; font-size: 30px; fill: var(--brown-dark); }
</style>
</head>
<body>
<svg class="label-sheet" viewBox="0 0 1200 1142" xmlns="http://www.w3.org/2000/svg">
  <defs>
    <linearGradient id="goldPaper" x1="0" y1="0" x2="1" y2="1">
      <stop offset="0" stop-color="var(--gold-light)"/>
      <stop offset="0.55" stop-color="var(--gold-mid)"/>
      <stop offset="1" stop-color="var(--gold-deep)"/>
    </linearGradient>
  </defs>

  <!-- Neck label -->
  <g class="neck-label">
    <path d="M 450 40 H 750 V 270 Q 700 300 650 285 Q 600 270 550 285 Q 500 300 450 270 Z"
          fill="url(#goldPaper)"/>
    <path d="M 450 250 Q 500 280 550 265 Q 600 250 650 265 Q 700 280 750 250"
          fill="none" stroke="var(--brown-mid)" stroke-width="3"/>
    <circle class="quality-seal" cx="600" cy="160" r="68" fill="var(--seal)"/>
  </g>

  <!-- Body label -->
  <g class="body-label">
    <ellipse cx="600" cy="730" rx="215" ry="360" fill="var(--brown-dark)"/>
    <ellipse cx="600" cy="730" rx="200" ry="345" fill="url(#goldPaper)"/>
    <ellipse cx="600" cy="730" rx="188" ry="333" fill="none" stroke="var(--brown-mid)" stroke-width="2"/>

    <ellipse class="leaf-crest" cx="600" cy="545" rx="150" ry="65" fill="var(--leaf)" opacity="0.75"
             role="img" aria-label="Fan of stylised brown leaves crowning the label"/>

    <g class="name-banner">
      <path d="M 420 645 Q 600 668 780 645 Q 768 682 780 725 Q 600 702 420 725 Q 432 682 420 645 Z"
            fill="var(--brown-dark)"/>
      <text class="brand-name" x="600" y="698" text-anchor="middle"
            textLength="300" lengthAdjust="spacingAndGlyphs">CORVEL'S HARD</text>
    </g>

    <text class="product-type" x="600" y="785" text-anchor="middle"
          textLength="270" lengthAdjust="spacingAndGlyphs">ROOT BEER</text>
    <text class="volume" x="600" y="925" text-anchor="middle">355 ml</text>
  </g>
</svg>
</body>
</html>
```